Business Card Design Project

I am a psychotherapist, counselor and expressive arts therapist (means I use every art form imaginable in the service of healing). I'm just starting out in private practice in San Francisco, CA. I work with individual adults, children and families. I'd like the card to mirror the simplicity and color palate of my website. I also would love if there is a symbol, image of fire, flame or spark (that is warming, not frightening).

Check out my website: www.lorabeckettmft.com

I want the cards to be printed in letter press so please keep that in mind!

Target Market(s)

Upper Middle Class Adults who are progressively minded, artistic or artists, open to psychotherapy, interested in health & healing.

Industry/Entity Type

Business

Requirements
Must have
• Text to be included:

Lora Beckett
Counseling, Psychotherapy & Expressive Arts

2814 Wexford Avenue, Suite F
San Francisco, CA 94127
p. 415.862.3097
lorajanebeckett@mailvane.net

www.lorabeckettmft.com

MFT License Number 68947

It's OK to abbreviate Number to # or Street to St., etc.

Must be compatible with letter press printing.
Nice to have
• I don't have a logo. I don't expect designers to necessarily create one for me, but if someone comes up with a simple image (see above about flame), that would be great. I don't have much of a budget now, but expect that to change in the next year or so and then could buy a logo for my website, future letterhead, etc.

```html
<!DOCTYPE html>
<html lang="en">
<head>
<meta charset="utf-8">
<title>Lora Beckett — Business Card</title>
<link rel="stylesheet" href="https://fonts.googleapis.com/css2?family=Belleza&display=swap">
<style>
  :root {
    --backdrop: #b9b9b9;
    --card: #ffffff;
    --ink: #d6581c;
    --accent: #f3b447;
    --shadow: rgba(0, 0, 0, 0.28);
  }
  * { box-sizing: border-box; margin: 0; padding: 0; }
  html, body {
    width: 1200px;
    height: 900px;
    overflow: hidden;
  }
  body {
    background: var(--backdrop);
    font-family: "Belleza", "Trebuchet MS", sans-serif;
    color: var(--ink);
    display: flex;
    flex-direction: column;
    align-items: center;
    justify-content: center;
    gap: 60px;
  }
  .card {
    position: relative;
    width: 630px;
    height: 360px;
    background: var(--card);
    box-shadow: 0 10px 26px var(--shadow);
  }

  /* Back of card: centred mark, tagline and web details */
  .card--back {
    display: flex;
    flex-direction: column;
    align-items: center;
    justify-content: center;
  }
  .mark {
    display: flex;
    align-items: center;
    gap: 12px;
    font-size: 30px;
    letter-spacing: 0.5px;
  }
  .mark__dot {
    display: block;
    width: 16px;
    height: 16px;
    border-radius: 50%;
    background: var(--accent);
  }
  .tagline {
    font-size: 22px;
    letter-spacing: 0.4px;
    margin-top: 24px;
  }
  .web {
    font-style: normal;
    text-align: center;
    font-size: 16px;
    line-height: 1.55;
    margin-top: 22px;
  }

  /* Front of card */
  .contact {
    position: absolute;
    right: 44px;
    top: 36px;
    text-align: right;
    font-style: normal;
    font-size: 16px;
    line-height: 1.55;
  }
  .identity {
    position: absolute;
    left: 48px;
    top: 150px;
  }
  .identity__name {
    font-size: 36px;
    font-weight: 400;
    line-height: 1.1;
  }
  .identity__role {
    font-size: 17px;
    margin-top: 4px;
  }
  .card--front .mark__dot {
    position: absolute;
    left: 210px;
    bottom: 44px;
    width: 40px;
    height: 40px;
  }
</style>
</head>
<body>
  <section class="card card--back" aria-label="Card back">
    <div class="mark">
      <span class="mark__dot"></span>
      <span class="mark__name">Lora Beckett</span>
    </div>
    <p class="tagline">Psychotherapy &amp; Expressive Arts</p>
    <address class="web">
      lorajanebeckett@mailvane.net<br>
      www.lorabeckettmft.com
    </address>
  </section>

  <section class="card card--front" aria-label="Card front">
    <address class="contact">
      p. 415.862.3097<br>
      2814 Wexford Avenue, Suite F<br>
      San Francisco, CA 94127<br>
      MFT License Number 68947
    </address>
    <div class="identity">
      <h1 class="identity__name">Lora Beckett</h1>
      <p class="identity__role">Counseling, Psychotherapy &amp; Expressive Arts</p>
    </div>
    <span class="mark__dot" aria-hidden="true"></span>
  </section>
</body>
</html>
```